World Wide News and Current Affairs website

We intends to start up a new website which deals on New and Current Affairs.
Attention Designers,
We want a home page design for this project. Our business is based in the United States. Our goal is to become a well known brand.
The website would consist of a category for News, Business and Tech.
The theme should be beautiful and attention seeking. The website would take bulk of it's news from the US, and Europe.
Designers can get inspiration from already existing new websites such as ZPW, VJL, HALDRIM.
All designs should be clean and easy to navigate.

```html
<!DOCTYPE html>
<html lang="en">
<head>
<meta charset="utf-8">
<title>DAYLINE – Home</title>
<link href="https://fonts.googleapis.com/css2?family=Montserrat:wght@400;500;600;700;800&family=Open+Sans:wght@400;600;700&display=swap" rel="stylesheet">
<style>
:root{
  --red:#d0122c;
  --orange:#f5a21b;
  --navy:#27338a;
  --navy-dark:#1d2570;
  --navy-panel:#2b37a0;
  --ink:#222;
  --muted:#777;
  --line:#e3e3e3;
  --gap:#eeeeee;
  --white:#fff;
  --footer:#1f2024;
  --yellow:#f8c327;
}
*{box-sizing:border-box;margin:0;padding:0}
html,body{width:1200px;height:3797px;overflow:hidden}
body{position:relative;background:var(--gap);font-family:'Open Sans',Arial,sans-serif;color:var(--ink);font-size:13px}
.abs{position:absolute}
.band{position:absolute;left:0;width:1200px;background:var(--white)}
.sec-title{position:absolute;font-family:'Montserrat',Arial,sans-serif;font-weight:700;font-size:19px;color:var(--navy);letter-spacing:.3px;text-transform:uppercase}
.sec-rule{position:absolute;height:2px;background:linear-gradient(90deg,var(--orange) 0 20%,var(--line) 20%)}
.more{position:absolute;font-family:'Montserrat',Arial,sans-serif;font-size:10px;font-weight:700;color:var(--navy);display:flex;align-items:center;gap:6px}
.more i{display:inline-block;width:18px;height:10px;background:var(--orange);border-radius:2px}
.photo{position:absolute;overflow:hidden}
.caption{position:absolute;left:14px;right:14px;bottom:14px;color:#fff;font-family:'Montserrat',Arial,sans-serif;font-weight:700;font-size:15px;line-height:1.25}
.tag{display:inline-block;background:var(--orange);color:#fff;font-family:'Montserrat',Arial,sans-serif;font-size:10px;font-weight:600;padding:2px 7px;margin-bottom:6px}
.shade{position:absolute;inset:0;background:linear-gradient(180deg,rgba(0,0,0,0) 45%,rgba(0,0,0,.78))}

/* header */
.header{position:absolute;left:0;top:0;width:1200px;height:71px;background:#fff}
.logo{position:absolute;left:144px;top:22px;display:flex;align-items:center;gap:8px;font-family:'Montserrat',Arial,sans-serif;font-weight:800;font-size:24px;color:var(--red)}
.logo b{width:14px;height:14px;border-radius:50%;background:var(--red);display:block}
.edition{position:absolute;right:145px;top:3px;font-family:'Montserrat',Arial,sans-serif;font-size:9px;color:var(--muted)}
.edition strong{color:var(--red)}
.navbar{position:absolute;left:330px;top:20px;width:870px;height:46px;background:var(--red);clip-path:polygon(30px 0,100% 0,100% 100%,0 100%)}
.nav{position:absolute;left:50px;top:0;height:46px;display:flex;align-items:center;gap:26px;font-family:'Montserrat',Arial,sans-serif;font-weight:600;font-size:12.5px;color:#fff}
.nav .home{color:var(--orange)}

/* hero */
.hero{position:absolute;left:0;top:71px;width:1200px;height:347px;background:#111}
.slide{position:absolute;top:0;height:347px}
.slide .body{position:absolute;left:26px;right:24px;bottom:18px;color:#fff}
.slide h2{font-family:'Montserrat',Arial,sans-serif;font-weight:700;font-size:22px;line-height:1.15;margin-bottom:12px}
.slide p{font-size:11px;line-height:1.5;color:#e4e4e4;margin-bottom:14px}
.read{font-family:'Montserrat',Arial,sans-serif;font-size:10.5px;font-weight:600;margin-bottom:10px}
.share{display:inline-block;background:var(--red);font-size:10px;font-weight:600;padding:3px 9px}
.breaking{position:absolute;right:0;top:110px;width:22px;height:120px;background:var(--orange);color:#fff;font-family:'Montserrat',Arial,sans-serif;font-size:10px;font-weight:700;writing-mode:vertical-rl;transform:rotate(180deg);text-align:center}
.dots{position:absolute;left:560px;bottom:10px;display:flex;gap:4px}
.dots span{width:8px;height:3px;background:#888}
.dots span.on{background:#fff}

/* top stories */
.stories{position:absolute;left:846px;top:494px;width:210px}
.stories li{list-style:none;font-size:11.5px;line-height:1.35;padding:9px 0;border-bottom:1px solid var(--line);color:#333}
.stories li.hot{background:#f2f2f2;font-weight:600;padding-left:4px}

/* weather */
.wx-now{position:absolute;left:144px;top:945px;width:180px;height:198px;border:1px solid var(--line);padding:14px 16px}
.wx-now h4{font-family:'Montserrat',Arial,sans-serif;font-size:16px;font-weight:600;color:#222}
.wx-now small{font-size:9px;color:var(--muted)}
.temp{font-family:'Montserrat',Arial,sans-serif;font-size:44px;font-weight:600;margin-top:14px}
.wx-days{position:absolute;left:327px;top:945px;width:496px;height:198px;display:flex;border:1px solid var(--line)}
.day{flex:1;text-align:center;padding-top:16px;border-right:1px solid var(--line);font-size:9.5px;color:var(--muted)}
.day:last-child{border-right:0}
.day h5{font-family:'Montserrat',Arial,sans-serif;font-size:14px;font-weight:500;color:#333;margin-bottom:20px}
.day.active{outline:2px solid var(--orange);outline-offset:-2px}
.ad{position:absolute;left:846px;top:891px;width:210px;height:256px;background:var(--yellow);text-align:center;font-family:'Montserrat',Arial,sans-serif}
.ad .pct{margin-top:66px;font-size:46px;font-weight:800;color:#222;line-height:1}
.ad .pct sup{font-size:18px}
.ad p{font-size:13px;font-weight:600;margin-top:16px;line-height:1.35}
.ad a{display:inline-block;margin-top:14px;background:#fff;color:var(--orange);font-size:11px;font-weight:700;padding:8px 16px;text-decoration:none}

/* market */
.market{position:absolute;left:144px;top:1253px;width:912px;height:329px;background:var(--navy-panel)}
.mtabs{position:absolute;left:0;top:0;width:912px;height:30px;background:var(--navy-dark);display:flex;font-family:'Montserrat',Arial,sans-serif;font-size:11px;font-weight:600;color:#cfd3f5}
.mtabs span{padding:8px 18px}
.mtabs .on{background:var(--orange);color:#fff}
.mbox{position:absolute;background:var(--navy-dark);color:#fff;font-size:10px}
.mrow{display:flex;justify-content:space-between;align-items:center;height:38px;padding:0 12px;border-top:1px solid rgba(255,255,255,.12)}
.mhead{display:flex;justify-content:space-between;padding:10px 12px;font-size:11px;font-weight:600}
.mhead em{font-style:normal;color:#99a0d8;font-size:9px;font-weight:400}
.up{background:#5fb83a;padding:1px 4px;font-size:9px}
.dn{color:#ff5a5a}
.gr{color:#6fd44a}

/* sports scores */
.scores{position:absolute;left:767px;top:1685px;width:289px;height:305px;border:1px solid var(--line);font-size:11px}
.scores h4{font-family:'Montserrat',Arial,sans-serif;font-size:15px;font-weight:600;padding:6px 10px;color:#222}
.dates{display:flex;justify-content:center;gap:7px;font-size:10px;color:#888;padding:8px 0;border-top:1px solid var(--line);border-bottom:1px solid var(--line)}
.dates .on{color:var(--red);font-weight:700}
.league{text-align:center;font-size:8.5px;color:#999;padding:8px 0 2px}
.match{display:flex;align-items:center;justify-content:space-between;height:62px;padding:0 14px;border-bottom:1px solid var(--line)}
.match .score{font-family:'Montserrat',Arial,sans-serif;font-weight:700;font-size:16px}
.crest{display:inline-block;width:20px;height:22px;border-radius:3px;vertical-align:middle;margin:0 6px}

/* tech list */
.tech-item{position:absolute;left:610px;width:446px;height:85px}
.tech-item .thumb{position:absolute;left:0;top:0;width:125px;height:75px}
.tech-item h6{position:absolute;left:143px;top:0;font-family:'Montserrat',Arial,sans-serif;font-size:12.5px;font-weight:500;color:#222}
.tech-item p{position:absolute;left:143px;top:20px;width:290px;font-size:10px;line-height:1.4;color:var(--muted)}
.tech-item .m{position:absolute;left:143px;top:55px}

/* video */
.play{position:absolute;border-radius:50%;border:3px solid #fff;display:flex;align-items:center;justify-content:center}
.vthumb{position:absolute;left:910px;width:146px;height:112px}
.vthumb .img{height:80px;position:relative}
.vthumb p{font-size:10px;color:#fff;line-height:1.25;padding:3px 5px}

/* footer */
.footer{position:absolute;left:0;top:3464px;width:1200px;height:333px;background:var(--footer);color:#bbb}
.fcol{position:absolute;top:66px;font-size:11px;line-height:2}
.fbottom{position:absolute;left:144px;top:252px;font-size:10px;color:#999;display:flex;gap:20px}
.copy{position:absolute;left:144px;top:276px;font-size:9.5px;color:#888}
.social{position:absolute;left:940px;top:250px;display:flex;gap:8px}
.social span{width:22px;height:22px;border-radius:50%;background:#555;display:block}
.subscribe{position:absolute;left:846px;top:125px;background:var(--red);color:#fff;font-family:'Montserrat',Arial,sans-serif;font-weight:600;font-size:12px;padding:9px 16px}
</style>
</head>
<body>

<header class="header">
  <div class="logo"><b></b>DAYLINE</div>
  <div class="edition">EDITION: <strong>UNITED STATES ▾</strong></div>
  <div class="navbar">
    <nav class="nav">
      <span class="home">⌂</span><span>U.S</span><span>Europe</span><span>World</span><span>Politics</span><span>Business</span><span>Markets</span><span>Tech</span><span>Auto</span><span>Money</span><span>Life</span><span>More ▾</span>
      <svg width="14" height="14" viewBox="0 0 14 14"><circle cx="6" cy="6" r="4.5" fill="none" stroke="#fff" stroke-width="2"/><line x1="9.5" y1="9.5" x2="13" y2="13" stroke="#fff" stroke-width="2"/></svg>
    </nav>
  </div>
</header>

<section class="hero">
  <article class="slide" style="left:0;width:291px">
    <div class="photo" role="img" aria-label="Football player celebrating in a stadium" style="inset:0;background:linear-gradient(160deg,#3a3f5a,#7a2a35 60%,#1a1a22)"></div>
    <div class="shade"></div>
    <div class="body"><span class="tag">Sports</span><h2>Consectetur sed do eiusmod tempor</h2><p>Duis aute irure dolor in reprehend in voluptate velit esse cillum ipsum dolor consectetur velit.</p><div class="read">Read More →</div><span class="share">&lt; Share</span></div>
  </article>
  <article class="slide" style="left:291px;width:620px">
    <div class="photo" role="img" aria-label="Politician speaking in front of a flag" style="inset:0;background:linear-gradient(120deg,#1d2236,#4a3b4f 40%,#9a3b3b 70%,#22283c)"></div>
    <div class="shade"></div>
    <div class="body" style="right:250px"><span class="tag">U.S</span><h2>Lorem ipsum dolor eiusmod sed do tempor</h2><p>Duis aute irure dolor in reprehend in voluptate velit esse cillum ipsum dolor consectetur velit ipsum eiusmod tempor aute irure dolor eu fugiat nulla.</p><div class="read">Read More →</div><span class="share">&lt; Share</span></div>
    <div class="dots"><span></span><span></span><span class="on"></span><span></span><span></span><span></span></div>
  </article>
  <article class="slide" style="left:911px;width:289px">
    <div class="photo" role="img" aria-label="City skyline at night" style="inset:0;background:linear-gradient(180deg,#1c2e4a,#2c4a6e 50%,#111a28)"></div>
    <div class="shade"></div>
    <div class="body"><span class="tag">Tech</span><h2>Consectetur sed do eiusmod tempor</h2><p>Duis aute irure dolor in reprehend in voluptate velit esse cillum ipsum dolor consectetur velit.</p><div class="read">Read More →</div><span class="share">&lt; Share</span></div>
    <div class="breaking">Breaking News</div>
  </article>
</section>

<section class="band" style="top:436px;height:420px">
  <h3 class="sec-title" style="left:144px;top:10px">Featured News</h3>
  <div class="more" style="left:768px;top:16px">MORE <i></i></div>
  <div class="sec-rule" style="left:144px;top:38px;width:616px"></div>

  <div class="photo" role="img" aria-label="Aircraft cabin" style="left:144px;top:58px;width:218px;height:159px;background:linear-gradient(150deg,#8fa0b0,#3f4c5a)"><div class="shade"></div><div class="caption">Consectetur sed do edu eiusmod tempor</div></div>
  <div class="photo" role="img" aria-label="Damaged building" style="left:144px;top:235px;width:218px;height:159px;background:linear-gradient(150deg,#a9a39a,#4d4a46)"><div class="shade"></div><div class="caption"><span class="tag">World</span><br>Consectetur sed do edu eiusmod tempor</div></div>
  <div class="photo" role="img" aria-label="Statue against a blue sky" style="left:380px;top:58px;width:207px;height:336px;background:linear-gradient(180deg,#6f9ac4,#c9a26a 55%,#4a3a28);outline:3px solid var(--orange);outline-offset:-3px"><div class="shade"></div><div class="caption">Consectetur sed do edu eiusmod tempor</div></div>
  <div class="photo" role="img" aria-label="Military vehicle" style="left:605px;top:58px;width:218px;height:159px;background:linear-gradient(150deg,#d9dcd8,#5b5e4e)"><div class="shade"></div><div class="caption"><span class="tag">World</span><br>Consectetur sed do edu eiusmod tempor</div></div>
  <div class="photo" role="img" aria-label="Woman in front of a flag" style="left:605px;top:235px;width:218px;height:159px;background:linear-gradient(150deg,#3c4a7a,#8a3a3a 55%,#2a2a30)"><div class="shade"></div><div class="caption"><span class="tag">U.S</span><br>Consectetur sed do edu eiusmod tempor</div></div>

  <h3 class="sec-title" style="left:846px;top:10px">Top Stories</h3>
  <div class="more" style="left:1020px;top:16px"><i></i></div>
  <div class="sec-rule" style="left:846px;top:38px;width:210px"></div>
  <ul class="stories" style="top:50px">
    <li>Skyvale Air employee to passenger: Hit me</li>
    <li>13 dead in 1 day in Venezuela protests</li>
    <li>Venezuela crisis: How paradise got lost</li>
    <li class="hot">Russia tried to use Harlan to infiltrate campaign – sources</li>
    <li>Dell Marsh responds to News report</li>
    <li>Orvell: US honors refugee deal with Australia</li>
    <li>Russia's more worried about war than US</li>
  </ul>
</section>

<section class="band" style="top:870px;height:296px">
  <h3 class="sec-title" style="left:144px;top:20px">Weather</h3>
  <div class="more" style="left:768px;top:26px">MORE <i></i></div>
  <div class="sec-rule" style="left:144px;top:48px;width:679px"></div>
</section>
<div class="wx-now">
  <h4>Newyork, U.S.A</h4><small>23 April 2017, Sunday</small>
  <div class="temp">23<sup style="font-size:18px">°</sup>
    <svg width="52" height="52" viewBox="0 0 52 52" style="vertical-align:middle;margin-left:16px"><circle cx="26" cy="26" r="11" fill="none" stroke="var(--orange)" stroke-width="3"/><g stroke="var(--orange)" stroke-width="3" stroke-linecap="round"><line x1="26" y1="3" x2="26" y2="9"/><line x1="26" y1="43" x2="26" y2="49"/><line x1="3" y1="26" x2="9" y2="26"/><line x1="43" y1="26" x2="49" y2="26"/><line x1="10" y1="10" x2="14" y2="14"/><line x1="38" y1="38" x2="42" y2="42"/><line x1="42" y1="10" x2="38" y2="14"/><line x1="10" y1="42" x2="14" y2="38"/></g></svg>
  </div>
  <div style="font-size:10px;color:#777;margin-top:6px">High: 23°&nbsp;&nbsp;&nbsp;&nbsp;Low: 18°</div>
  <div style="font-size:8px;color:var(--navy);font-weight:700;margin-top:16px;text-align:center">NEXT CITY</div>
</div>
<div class="wx-days">
  <div class="day"><h5>Mon</h5><svg width="54" height="40" viewBox="0 0 54 40"><path d="M12 34a9 9 0 0 1 2-18 13 13 0 0 1 25-2 10 10 0 0 1 3 20z" fill="none" stroke="var(--navy)" stroke-width="2.5"/></svg><p style="margin-top:18px">High: 23°&nbsp; Low: 18°</p></div>
  <div class="day"><h5>Tue</h5><svg width="54" height="40" viewBox="0 0 54 40"><circle cx="34" cy="12" r="7" fill="none" stroke="var(--orange)" stroke-width="2.5"/><path d="M10 34a8 8 0 0 1 2-16 12 12 0 0 1 23-2 9 9 0 0 1 3 18z" fill="#fff" stroke="var(--navy)" stroke-width="2.5"/></svg><p style="margin-top:18px">High: 23°&nbsp; Low: 18°</p></div>
  <div class="day active"><h5>Wed</h5><svg width="54" height="44" viewBox="0 0 54 44"><path d="M12 30a9 9 0 0 1 2-18 13 13 0 0 1 25-2 10 10 0 0 1 3 20z" fill="none" stroke="var(--navy)" stroke-width="2.5"/><g stroke="var(--navy)" stroke-width="2"><line x1="18" y1="35" x2="16" y2="41"/><line x1="27" y1="35" x2="25" y2="41"/><line x1="36" y1="35" x2="34" y2="41"/></g></svg><p style="margin-top:14px">High: 23°&nbsp; Low: 18°</p></div>
  <div class="day"><h5>Thu</h5><svg width="54" height="44" viewBox="0 0 54 44"><path d="M12 30a9 9 0 0 1 2-18 13 13 0 0 1 25-2 10 10 0 0 1 3 20z" fill="none" stroke="var(--navy)" stroke-width="2.5"/><g stroke="var(--navy)" stroke-width="2"><line x1="22" y1="35" x2="20" y2="41"/><line x1="32" y1="35" x2="30" y2="41"/></g></svg><p style="margin-top:14px">High: 23°&nbsp; Low: 18°</p></div>
  <div class="day"><h5>Fri</h5><svg width="54" height="40" viewBox="0 0 54 40"><circle cx="34" cy="12" r="7" fill="none" stroke="var(--orange)" stroke-width="2.5"/><path d="M10 34a8 8 0 0 1 2-16 12 12 0 0 1 23-2 9 9 0 0 1 3 18z" fill="#fff" stroke="var(--navy)" stroke-width="2.5"/></svg><p style="margin-top:18px">High: 23°&nbsp; Low: 18°</p></div>
  <div class="day"><h5>Sat</h5><svg width="54" height="40" viewBox="0 0 54 40"><path d="M12 34a9 9 0 0 1 2-18 13 13 0 0 1 25-2 10 10 0 0 1 3 20z" fill="none" stroke="var(--navy)" stroke-width="2.5"/></svg><p style="margin-top:18px">High: 23°&nbsp; Low: 18°</p></div>
</div>
<aside class="ad">
  <div class="pct">50<sup>%</sup><br><span style="font-size:20px">OFF</span></div>
  <p>You Shop We Ship<br>For Free</p>
  <a>SHOP NOW!</a>
</aside>

<section class="band" style="top:1188px;height:420px">
  <h3 class="sec-title" style="left:144px;top:22px">Market</h3>
  <div class="more" style="left:1000px;top:28px">MORE <i></i></div>
  <div class="sec-rule" style="left:144px;top:50px;width:912px"></div>
</section>
<div class="market">
  <div class="mtabs"><span class="on">U.S.</span><span>EUROPE</span><span>ASIA</span><span>SECTORS</span></div>
  <div class="mbox" style="left:14px;top:40px;width:210px;height:276px">
    <div class="mhead">Market Indices <em>View All</em></div>
    <div class="mrow" style="outline:2px solid var(--orange);outline-offset:-2px"><span>IND 30</span><span>20,547.76</span><span class="up">+4.75</span></div>
    <div class="mrow"><span>US 500</span><span>2,348.69</span><span class="up">+4.75</span></div>
    <div class="mrow"><span>TECH 100</span><span>5,910.52</span><span class="up">+4.75</span></div>
    <div class="mrow"><span>US TOTAL</span><span>201.46</span><span class="up">+4.75</span></div>
  </div>
  <svg class="abs" style="left:232px;top:40px" width="330" height="276" viewBox="0 0 330 276">
    <circle cx="72" cy="44" r="30" fill="var(--navy-dark)" stroke="var(--orange)" stroke-width="2"/>
    <text x="72" y="36" fill="#fff" font-size="8" text-anchor="middle" font-family="Open Sans">IND 30</text>
    <text x="72" y="49" fill="#fff" font-size="10" font-weight="700" text-anchor="middle" font-family="Open Sans">20,547.76</text>
    <text x="72" y="60" fill="#6fd44a" font-size="8" text-anchor="middle" font-family="Open Sans">+4.75</text>
    <g font-family="Open Sans" font-size="9" fill="#c7cbf0"><text x="150" y="30">OPEN</text><text x="150" y="48">HIGH</text><text x="150" y="66">LOW</text><text x="200" y="30">20,547.31</text><text x="200" y="48">20,549.16</text><text x="200" y="66">20,543.81</text></g>
    <g stroke="rgba(255,255,255,.12)"><line x1="20" y1="100" x2="290" y2="100"/><line x1="20" y1="140" x2="290" y2="140"/><line x1="20" y1="180" x2="290" y2="180"/><line x1="20" y1="220" x2="290" y2="220"/></g>
    <path d="M20 150 L40 140 L55 118 L70 108 L85 122 L100 112 L115 130 L130 122 L150 140 L165 132 L180 150 L195 145 L210 172 L225 180 L240 165 L255 190 L270 182 L290 200 L290 240 L20 240Z" fill="rgba(111,212,74,.18)"/>
    <path d="M20 150 L40 140 L55 118 L70 108 L85 122 L100 112 L115 130 L130 122 L150 140 L165 132 L180 150 L195 145 L210 172 L225 180 L240 165 L255 190 L270 182 L290 200" fill="none" stroke="#6fd44a" stroke-width="2"/>
    <g font-family="Open Sans" font-size="7" fill="#c7cbf0"><text x="298" y="103">19,820</text><text x="298" y="143">19,760</text><text x="298" y="183">19,700</text><text x="298" y="223">19,640</text><text x="30" y="256">9:30</text><text x="100" y="256">11:00</text><text x="170" y="256">12:30</text><text x="240" y="256">14:00</text></g>
  </svg>
  <div class="mbox" style="left:605px;top:40px;width:140px;height:276px">
    <div class="mhead">Currencies <em>View All</em></div>
    <div class="mrow"><span>EUR/USD</span><span>1.0726</span><span class="gr">+0.05%</span></div>
    <div class="mrow"><span>GBP/USD</span><span>1.2812</span><span class="gr">+0.05%</span></div>
    <div class="mrow"><span>USD/JPY</span><span>109.14</span><span class="gr">+0.05%</span></div>
    <div class="mrow"><span>USD/CHF</span><span>0.9958</span><span class="gr">+0.05%</span></div>
  </div>
  <div class="mbox" style="left:755px;top:40px;width:143px;height:276px">
    <div class="mhead">Commodities <em>View All</em></div>
    <div class="mrow"><span>GOLD</span><span>1,283.10</span><span class="gr">+0.25%</span></div>
    <div class="mrow"><span>OIL</span><span>49.65</span><span class="dn">-0.15%</span></div>
    <div class="mrow"><span>COPPER</span><span>258.50</span><span class="gr">+0.25%</span></div>
    <div class="mrow"><span>GAS</span><span>49.65</span><span class="dn">-0.15%</span></div>
  </div>
</div>

<section class="band" style="top:1630px;height:398px">
  <h3 class="sec-title" style="left:144px;top:18px">Sports</h3>
  <div class="more" style="left:1000px;top:24px">MORE <i></i></div>
  <div class="sec-rule" style="left:144px;top:46px;width:912px"></div>
  <div class="photo" role="img" aria-label="Football team celebrating with a trophy" style="left:144px;top:66px;width:596px;height:294px;background:linear-gradient(150deg,#7a1d22,#b8323a 45%,#2a1a1c)">
    <div class="shade"></div>
    <div class="caption" style="left:26px;bottom:26px;font-size:19px">Consectetur sed do edu eiusmod tempor lorem ipsum
      <p style="font-family:'Open Sans',sans-serif;font-weight:400;font-size:10.5px;line-height:1.5;margin-top:8px;color:#ddd">Duis aute irure dolor in reprehend in voluptate velit esse cillum ipsum dolor consectetur velit ipsum eiusmod tempor aute irure dolor eu fugiat nulla pariatur.</p>
      <p style="font-size:10.5px;margin-top:8px">Read More →</p></div>
  </div>
</section>
<div class="scores">
  <h4>Football Scores</h4>
  <div class="dates"><span>17</span><span>18</span><span>19</span><span>20</span><span>21</span><span class="on">22</span><span>23</span><span>24</span><span>25</span></div>
  <div class="league">PREMIER DIVISION</div>
  <div class="match" style="border-top:1px solid var(--line)"><span>Ashford Rovers<span class="crest" style="background:#c4161c"></span></span><span class="score">4 0</span><span><span class="crest" style="background:#d91f2a"></span>Millbrook</span></div>
  <div class="match"><span>Harlow Town<span class="crest" style="background:#f2a900"></span></span><span class="score">2 0</span><span><span class="crest" style="background:#f5d000"></span>Wexley</span></div>
  <div class="match"><span>Seaton City<span class="crest" style="background:#333"></span></span><span class="score">2 0</span><span><span class="crest" style="background:#d0122c"></span>Stanmore City</span></div>
</div>

<section class="band" style="top:2036px;height:386px">
  <h3 class="sec-title" style="left:144px;top:20px">Business</h3>
  <div class="more" style="left:535px;top:26px">MORE <i></i></div>
  <div class="sec-rule" style="left:144px;top:48px;width:443px"></div>
  <div class="photo" role="img" aria-label="Business leader speaking at a conference" style="left:144px;top:72px;width:443px;height:278px;background:linear-gradient(150deg,#2a3a5a,#1a2034 60%,#0e1220)"><div class="shade"></div><div class="caption" style="left:18px;bottom:18px;font-size:14px">Consectetur sed do aute irure eiusmod tempor dolor consectetur velit</div></div>

  <h3 class="sec-title" style="left:610px;top:20px">Tech</h3>
  <div class="more" style="left:1000px;top:26px">MORE <i></i></div>
  <div class="sec-rule" style="left:610px;top:48px;width:446px"></div>
</section>
<div class="tech-item" style="top:2108px"><div class="thumb" role="img" aria-label="Hands holding a smartphone" style="background:linear-gradient(135deg,#c9b8a4,#6a5a4a)"></div><h6>Molore eu fugiat nulla pariatur esse dolor</h6><p>Duis aute irure dolor in reprehend in voluptate velit esse cillum dolore consectetur</p><div class="more m">MORE <i></i></div></div>
<div class="tech-item" style="top:2206px"><div class="thumb" role="img" aria-label="Laptop on a desk" style="background:linear-gradient(135deg,#b7c4cf,#4a5662)"></div><h6>Molore eu fugiat nulla pariatur esse dolor</h6><p>Duis aute irure dolor in reprehend in voluptate velit esse cillum dolore consectetur</p><div class="more m">MORE <i></i></div></div>
<div class="tech-item" style="top:2304px"><div class="thumb" role="img" aria-label="Office workspace with computers" style="background:linear-gradient(135deg,#d8d8d8,#555)"></div><h6>Molore eu fugiat nulla pariatur esse dolor</h6><p>Duis aute irure dolor in reprehend in voluptate velit esse cillum dolore consectetur</p><div class="more m">MORE <i></i></div></div>

<section class="band" style="top:2430px;height:384px">
  <h3 class="sec-title" style="left:144px;top:20px">Politics</h3>
  <div class="more" style="left:535px;top:26px">MORE <i></i></div>
  <div class="sec-rule" style="left:144px;top:48px;width:443px"></div>
  <div class="photo" role="img" aria-label="Two leaders shaking hands at a climate summit" style="left:144px;top:72px;width:443px;height:278px;background:linear-gradient(180deg,#e8e8e8,#9a9a9a 55%,#3a3a40)"><div class="shade"></div><div class="caption" style="left:18px;bottom:18px;font-size:14px">Consectetur sed do aute irure eiusmod tempor dolor consectetur velit</div></div>

  <h3 class="sec-title" style="left:610px;top:20px">World</h3>
  <div class="more" style="left:1000px;top:26px">MORE <i></i></div>
  <div class="sec-rule" style="left:610px;top:48px;width:446px"></div>
  <div class="photo" role="img" aria-label="Icebergs floating in a cold sea" style="left:610px;top:72px;width:446px;height:278px;background:linear-gradient(180deg,#9fb4c8,#e6eef3 40%,#2d5873 70%,#12324a)"><div class="shade"></div><div class="caption" style="left:18px;bottom:18px;font-size:14px">Consectetur sed do aute irure eiusmod tempor dolor consectetur velit</div></div>
</section>

<section class="band" style="top:2822px;height:612px">
  <h3 class="sec-title" style="left:144px;top:22px">Video</h3>
  <div class="sec-rule" style="left:144px;top:50px;width:912px"></div>
  <div class="photo" role="img" aria-label="Refugees arriving on a shore" style="left:144px;top:78px;width:756px;height:482px;background:linear-gradient(150deg,#4a5a6a,#8a4a3a 45%,#2a2e36)">
    <div class="shade"></div>
    <div class="play" style="left:343px;top:195px;width:74px;height:74px"><svg width="26" height="30" viewBox="0 0 26 30"><path d="M2 1 L25 15 L2 29Z" fill="#fff"/></svg></div>
    <div class="caption" style="left:24px;bottom:48px;font-size:24px">Consectetur sed do edu eiusmod tempor</div>
    <p class="abs" style="left:24px;bottom:14px;width:560px;color:#ddd;font-size:10.5px;line-height:1.45">Duis aute irure dolor in reprehend in voluptate velit esse cillum ipsum dolor consectetur velit ipsum eiusmod tempor nulla pariatur.</p>
  </div>
  <div class="photo" style="left:900px;top:78px;width:156px;height:482px;background:#2b2b30"></div>
</section>
<div class="vthumb" style="top:2905px"><div class="img" role="img" aria-label="Ship at sea" style="background:linear-gradient(135deg,#c55a3a,#3a2a2a)"><div class="play" style="left:58px;top:25px;width:30px;height:30px;border-width:2px"><svg width="10" height="12"><path d="M1 0 L10 6 L1 12Z" fill="#fff"/></svg></div></div><p>Molore eu fugiat nulla pariatur esse</p></div>
<div class="vthumb" style="top:3025px"><div class="img" role="img" aria-label="Crowd at a rally" style="background:linear-gradient(135deg,#7a6a8a,#2a2030)"><div class="play" style="left:58px;top:25px;width:30px;height:30px;border-width:2px"><svg width="10" height="12"><path d="M1 0 L10 6 L1 12Z" fill="#fff"/></svg></div></div><p>Molore eu fugiat nulla pariatur esse</p></div>
<div class="vthumb" style="top:3145px"><div class="img" role="img" aria-label="Street at dusk" style="background:linear-gradient(135deg,#b86a3a,#3a2a40)"><div class="play" style="left:58px;top:25px;width:30px;height:30px;border-width:2px"><svg width="10" height="12"><path d="M1 0 L10 6 L1 12Z" fill="#fff"/></svg></div></div><p>Molore eu fugiat nulla pariatur esse</p></div>
<div class="vthumb" style="top:3265px"><div class="img" role="img" aria-label="Coastline with boats" style="background:linear-gradient(135deg,#6a8aa8,#2a3a4a)"><div class="play" style="left:58px;top:25px;width:30px;height:30px;border-width:2px"><svg width="10" height="12"><path d="M1 0 L10 6 L1 12Z" fill="#fff"/></svg></div></div><p>Molore eu fugiat nulla pariatur esse</p></div>

<footer class="footer">
  <div class="logo" style="top:84px;color:#fff"><b style="background:#fff"></b>DAYLINE</div>
  <div class="fcol" style="left:355px">U.S<br>Europe<br>World<br>Politics</div>
  <div class="fcol" style="left:478px">Business<br>Market<br>Tech<br>Auto</div>
  <div class="fcol" style="left:607px">Opinion<br>Money<br>Life<br>Food</div>
  <div class="fcol" style="left:737px">Shop<br>Future<br>Nature<br>TV</div>
  <p class="abs" style="left:846px;top:70px;width:210px;font-size:10.5px;line-height:1.5;color:#bbb">Duis aute irure dolor in reprehend in to voluptate velit esse cillum ipsum.</p>
  <div class="subscribe">Subscribe Now</div>
  <div class="abs" style="left:144px;top:236px;width:912px;height:1px;background:#333"></div>
  <div class="fbottom"><span>Desktop Site</span><span>Terms of Use</span><span>About the VJL</span><span>Privacy Policy</span><span>Cookies</span><span>Contact the Newsroom</span><span>Advertise with us</span><span>Ad choices</span></div>
  <div class="copy">Copyright © 2017 DAYLINE. DAYLINE is not responsible for the content of external sites.</div>
  <div class="social"><span></span><span></span><span></span><span></span></div>
</footer>

</body>
</html>
```